Vorlage für ein Workbook
Zielgruppe
Coaching und Beratung
Aufgabenstellung
Es soll eine Vorlage für ein Workbook erstellt werden, das ich dann selbst mit Inhalten füllen kann.. evtl. mit Canvas oder wie auch immer....
Es ist ein 12 Wochenkurs, d.h. ich brauche 1 Titelseite für jede Woche, die ich dann paste und copy machen kann und beschriften kann, sowie eine Vorlage für die einzelnen Seiten des Workbooks. Das Workbook in pdf Format muss auch online ausgefüllt werden können.
Design angepasst an Landingpage

```html
<!DOCTYPE html>
<html lang="de">
<head>
<meta charset="utf-8">
<title>Workbook Vorlage – Wochenseiten</title>
<link href="https://fonts.googleapis.com/css2?family=Cinzel:wght@400&display=swap" rel="stylesheet">
<style>
  :root {
    --paper: #ffffff;
    --taupe: #c5bdb6;
    --sage: #b3bea6;
    --mist: #c8d0d9;
    --line: #f7ece6;
    --botanical: #d6cdc6;
  }
  * { box-sizing: border-box; margin: 0; padding: 0; }
  html, body { width: 865px; height: 1200px; overflow: hidden; background: var(--paper); }
  .sheet { position: relative; width: 865px; height: 1200px; }
  .page {
    position: absolute; width: 395px; height: 560px;
    background: var(--taupe); overflow: hidden;
  }
  .page--one   { left: 25px;  top: 27px; }
  .page--two   { left: 444px; top: 27px; }
  .page--three { left: 25px;  top: 608px; }
  .page--four  { left: 444px; top: 608px; }
  .page__art { position: absolute; inset: 0; width: 100%; height: 100%; }
  .blob--sage { fill: var(--sage); }
  .blob--mist { fill: var(--mist); }
  .flow-line { fill: none; stroke: var(--line); stroke-width: 1.6; }
  .botanical {
    position: absolute; background: var(--botanical);
    opacity: .55; border-radius: 45% 55% 50% 50%;
  }
  .page__text { position: absolute; left: 68px; top: 202px; width: 300px; color: var(--line); font-family: 'Cinzel', serif; }
  .page__title { font-size: 33px; font-weight: 400; letter-spacing: .5px; line-height: 1; }
  .page__lead { margin-top: 9px; font-size: 7.2px; line-height: 1.3; letter-spacing: .1px; }
</style>
</head>
<body>
<main class="sheet">

  <section class="page page--one">
    <svg class="page__art" viewBox="0 0 594 842" preserveAspectRatio="none" aria-hidden="true">
      <path class="blob--sage" d="M385 0H594V200C540 200 515 180 505 150C495 110 500 60 460 30C440 15 400 10 385 0Z"/>
      <path class="blob--sage" d="M0 645C60 638 140 650 180 690C220 720 300 700 340 730C370 760 360 800 420 805C500 805 570 805 594 840V842H0Z"/>
      <path class="flow-line" d="M0 520C80 515 140 540 150 600C165 690 170 740 215 735C300 725 430 720 470 842"/>
      <path class="flow-line" d="M0 560C90 550 150 600 135 650C110 720 160 830 240 825C330 815 400 770 440 842"/>
    </svg>
    <div class="botanical" style="left:0;top:0;width:150px;height:175px" role="img" aria-label="Zweig mit Blättern und Beeren, weiße Linienzeichnung"></div>
    <div class="botanical" style="left:334px;top:0;width:61px;height:125px" role="img" aria-label="Kleiner Zweig mit Beeren, weiße Linienzeichnung"></div>
    <div class="page__text">
      <h1 class="page__title">Lorem Ipsum</h1>
      <p class="page__lead">Lorem ipsum dolor sit amet, consectetuer adipiscing elit,<br>sed diam nonummy nibh euismod tincidunt ut laoreet<br>dolore magna aliquam</p>
    </div>
  </section>

  <section class="page page--two">
    <svg class="page__art" viewBox="0 0 594 842" preserveAspectRatio="none" aria-hidden="true">
      <path class="blob--mist" d="M0 0H594V30C590 80 560 120 440 140C300 160 150 145 90 200C55 235 25 270 0 300Z"/>
      <path class="flow-line" d="M0 50C80 30 200 60 250 100C310 150 290 30 380 0"/>
      <path class="flow-line" d="M0 95C90 85 170 110 210 150C250 190 300 190 330 120C360 50 380 20 390 0"/>
      <path class="flow-line" d="M220 842C300 800 320 600 350 520C400 440 560 480 594 380"/>
      <path class="flow-line" d="M390 842C410 700 390 600 450 590C520 580 560 610 594 640"/>
    </svg>
    <div class="botanical" style="left:0;top:350px;width:160px;height:205px" role="img" aria-label="Blätterzweig, weiße Linienzeichnung"></div>
    <div class="page__text">
      <h2 class="page__title">Lorem Ipsum</h2>
      <p class="page__lead">Lorem ipsum dolor sit amet, consectetuer adipiscing elit,<br>sed diam nonummy nibh euismod tincidunt ut laoreet<br>dolore magna aliquam</p>
    </div>
  </section>

  <section class="page page--three">
    <svg class="page__art" viewBox="0 0 594 842" preserveAspectRatio="none" aria-hidden="true">
      <path class="blob--sage" d="M380 0H594V160C560 180 525 170 512 140C500 110 480 118 440 125C380 132 368 90 380 60Z"/>
      <path class="flow-line" d="M345 0C350 80 340 170 390 190C450 200 500 180 520 220C550 270 580 262 594 265"/>
      <path class="flow-line" d="M385 0C360 60 375 120 400 150C420 175 470 170 500 200"/>
      <path class="blob--sage" d="M0 390C50 380 80 420 75 470C70 520 120 560 200 580C280 600 340 640 380 700C390 760 385 810 380 842H0Z"/>
      <path class="flow-line" d="M0 450C50 470 60 560 60 630C70 700 100 720 160 730C260 730 360 760 390 842"/>
    </svg>
    <div class="botanical" style="left:0;top:50px;width:150px;height:98px" role="img" aria-label="Blätterzweig, weiße Linienzeichnung"></div>
    <div class="page__text">
      <h2 class="page__title">Lorem Ipsum</h2>
      <p class="page__lead">Lorem ipsum dolor sit amet, consectetuer adipiscing elit,<br>sed diam nonummy nibh euismod tincidunt ut laoreet<br>dolore magna aliquam</p>
    </div>
  </section>

  <section class="page page--four">
    <svg class="page__art" viewBox="0 0 594 842" preserveAspectRatio="none" aria-hidden="true">
      <path class="blob--sage" d="M210 0H594V455C540 455 510 420 510 380C510 310 440 270 350 270C300 270 300 220 300 180C300 130 280 110 250 90C220 60 215 30 210 0Z"/>
      <path class="flow-line" d="M210 0C230 50 300 70 330 100C360 130 420 120 500 160C570 190 575 280 580 350C585 420 594 470 594 480"/>
      <path class="blob--mist" d="M0 610C80 600 130 640 140 720C150 780 200 830 290 842H0Z"/>
    </svg>
    <div class="botanical" style="left:186px;top:326px;width:209px;height:234px" role="img" aria-label="Zweig mit Blättern und Beeren, weiße Linienzeichnung"></div>
    <div class="page__text">
      <h2 class="page__title">Lorem Ipsum</h2>
      <p class="page__lead">Lorem ipsum dolor sit amet, consectetuer adipiscing elit,<br>sed diam nonummy nibh euismod tincidunt ut laoreet<br>dolore magna aliquam</p>
    </div>
  </section>

</main>
</body>
</html>
```